Looking for a "Hipster orientated" menu design for our espresso bar.
Lantern Brewhouse is part of the Marlow Kettle Group a leading Australian roasting company.
We are leaving the brief open as we don't to use any pre-conceived ideas that are in our heads. In a nutshell we don't want to be an imitation of others.
Lantern Brewhouse is an industrial inspired space with some classic elements. Coffee is our passion and simple fresh well presented food to match using the best local ingredients.

We would like our menu to have a clear distinction between beverages and food.
An open A4 size menu landscape format is ideal or perhaps folded.

This is our first crowd sourced design and the menu is a test to what will be a new webpage, online store and new brand elements for our company to the right designer.

At this stage don't worry about content i.e whats in a sandwich. Random latin under the word breakfast burger is fine.

Good luck

Target Market(s)

Hipster caffeine and food addicts

Industry/Entity Type

Industrial

Font styles to use
Decorative

Colors

Designer to choose colors to be used in the design.

Requirements
Must have
• A distinction between breakfast, lunch and beverages/coffee
Should not have
• overcrowded, hard to read

```html
<!DOCTYPE html>
<html lang="en">
<head>
<meta charset="utf-8">
<title>Lantern Brewhouse — Menu</title>
<link href="https://fonts.googleapis.com/css2?family=Bebas+Neue&family=Oswald:wght@400;500;600&family=Open+Sans:wght@400&family=Special+Elite&display=swap" rel="stylesheet">
<style>
  :root{
    --paper:#f4f3f1;
    --paper-white:#fbfbfa;
    --ink:#4b413b;
    --ink-dark:#4e4540;
    --body:#6d645e;
    --gold:#c08a32;
    --sand:#dcd7cf;
    --light:#efe9df;
    --rule:#4b413b;
  }
  *{margin:0;padding:0;box-sizing:border-box}
  html,body{width:927px;height:1200px;overflow:hidden;background:var(--paper)}
  .menu{position:relative;width:927px;height:1200px;background:var(--paper);color:var(--ink);font-family:"Open Sans",sans-serif}

  .band{position:absolute;left:0;width:927px}
  .band--breakfast{top:0;height:295px;background:var(--paper-white)}
  .band--lunch{top:295px;height:478px;background:var(--paper)}
  .band--drinks{top:773px;height:427px;background:var(--paper-white)}
  .rule-h{position:absolute;height:3px;background:var(--rule)}
  .rule-v{position:absolute;width:2px;background:var(--rule)}
  .rule-thin{position:absolute;height:1px;background:#8d847d}

  .section-title{position:absolute;writing-mode:vertical-rl;transform:rotate(180deg);font-family:"Bebas Neue",sans-serif;font-size:50px;letter-spacing:3px;color:var(--ink);text-align:center;line-height:1}
  .sub-title{position:absolute;writing-mode:vertical-rl;transform:rotate(180deg);font-family:"Oswald",sans-serif;font-weight:400;font-size:15px;letter-spacing:3px;text-transform:uppercase;color:var(--ink);text-align:center;line-height:1}

  .item{position:absolute;width:158px}
  .item-name{font-family:"Oswald",sans-serif;font-weight:600;font-size:12px;text-transform:uppercase;color:var(--ink);white-space:nowrap;line-height:16px}
  .item-price{color:var(--gold);font-weight:500;margin-left:4px}
  .item-desc{font-size:10px;line-height:12px;color:var(--body)}
  .item--wide{width:300px}
  .drink{position:absolute;font-family:"Oswald",sans-serif;font-weight:600;font-size:12.5px;color:var(--ink);white-space:nowrap}
  .drink .item-price{margin-left:10px}
  .drink-note{position:absolute;font-size:10px;color:var(--body)}

  .special-panel{position:absolute;left:609px;top:0;width:148px;height:288px;background:var(--sand);text-align:center;padding-top:18px}
  .special-title{font-family:"Oswald",sans-serif;font-weight:600;font-size:14px;color:var(--ink);letter-spacing:.5px}
  .special-item{font-family:"Oswald",sans-serif;font-size:12px;letter-spacing:1.5px;color:var(--ink);margin-top:20px}
  .special-note{font-size:9px;line-height:10px;color:var(--body);padding:0 14px}
  .special-or{margin:12px 12px 0;border-top:1px dotted var(--ink);position:relative;height:10px}
  .special-or span{position:absolute;left:50%;top:-7px;transform:translateX(-50%);background:var(--sand);padding:0 4px;font-size:9px;color:var(--body)}
  .special-served{font-family:"Oswald",sans-serif;font-size:9px;line-height:11px;color:var(--gold);text-transform:uppercase;margin-top:18px;padding:0 10px}
  .seal{position:absolute;left:58px;top:248px;width:32px;height:32px;border-radius:50%;background:#c7bfb3}

  .brand-panel{position:absolute;left:762px;top:0;width:165px;height:288px;background:var(--ink-dark);text-align:center;color:var(--light)}
  .brand-name{font-family:"Oswald",sans-serif;font-weight:500;font-size:21px;letter-spacing:2px;line-height:28px;margin-top:28px;color:var(--light)}
  .promo-ring{position:absolute;left:35px;top:150px;width:96px;height:96px;border-radius:50%;border:2px solid #cfc6bb;display:flex;align-items:center;justify-content:center;font-family:"Special Elite",monospace;font-size:15px;line-height:19px;color:var(--light)}

  .fresh-tag{position:absolute;left:774px;top:325px;width:150px;transform:rotate(-7deg);text-align:center;font-family:"Special Elite",monospace;font-size:13px;line-height:17px;letter-spacing:1px;color:var(--ink);border-top:2px solid var(--ink);border-bottom:2px solid var(--ink);padding:6px 0}

  .tip-box{position:absolute;left:818px;top:530px;width:109px;height:197px;background:var(--ink-dark);color:var(--light);font-family:"Special Elite",monospace;font-size:15px;line-height:19px;text-align:center;padding-top:16px;letter-spacing:.5px}

  .desserts-title{position:absolute;left:545px;top:803px;width:170px;height:44px;border-top:2px solid var(--ink);border-bottom:2px solid var(--ink);transform:rotate(-4deg);font-family:"Bebas Neue",sans-serif;font-size:40px;letter-spacing:3px;text-align:center;line-height:44px;color:var(--ink)}
  .dessert-seal{position:absolute;left:690px;top:1120px;width:42px;height:42px;border-radius:50%;background:#b9a591}

  .veggie-flourish{position:absolute;left:828px;top:815px;width:90px;height:20px;background:linear-gradient(90deg,transparent,#cfc8c0,transparent)}
  .veggie-flourish--low{top:970px}
  .veggie-title{position:absolute;left:818px;top:852px;width:109px;text-align:center;font-family:"Special Elite",monospace;font-size:19px;line-height:34px;color:var(--ink)}
  .veggie-note{position:absolute;left:818px;top:1008px;width:109px;text-align:center;font-family:"Special Elite",monospace;font-size:14px;line-height:21px;color:var(--ink)}
</style>
</head>
<body>
<main class="menu">

  <section class="band band--breakfast" aria-label="Breakfast">
    <h2 class="section-title" style="left:14px;top:0;height:295px">Breakfast</h2>
    <div class="rule-v" style="left:73px;top:0;height:295px"></div>

    <div class="item" style="left:121px;top:34px"><p class="item-name">Lantern Brewhouse<span class="item-price">$5.25</span></p><p class="item-desc">Some of our restaurant menus, prices and special offers may vary.</p></div>
    <div class="item" style="left:285px;top:34px"><p class="item-name">Lantern Brewhouse<span class="item-price">$5.25</span></p><p class="item-desc">some of our restaurant menus, prices and special offers may vary.</p></div>
    <div class="item" style="left:447px;top:34px"><p class="item-name">Lantern Brewhouse<span class="item-price">$5.25</span></p><p class="item-desc">some of our restaurant menus, prices and special offers may vary.</p></div>

    <div class="item" style="left:121px;top:102px"><p class="item-name">Lantern Brewhouse<span class="item-price">$5.25</span></p><p class="item-desc">Some of our restaurant menus, prices and special offers may vary.</p></div>
    <div class="item" style="left:285px;top:102px"><p class="item-name">Lantern Brewhouse<span class="item-price">$5.25</span></p><p class="item-desc">some of our restaurant menus, prices and special offers may vary.</p></div>
    <div class="item" style="left:447px;top:102px"><p class="item-name">Lantern Brewhouse<span class="item-price">$5.25</span></p><p class="item-desc">some of our restaurant menus, prices and special offers may vary.</p></div>

    <div class="item" style="left:121px;top:172px"><p class="item-name">Lantern Brewhouse<span class="item-price">$5.25</span></p><p class="item-desc">some of our restaurant menus, prices and special offers may vary depending on locally sourced items.</p></div>
    <div class="item" style="left:285px;top:172px"><p class="item-name">Lantern Brewhouse<span class="item-price">$5.25</span></p><p class="item-desc">some of our restaurant menus, prices and special offers may vary.</p></div>
    <div class="item" style="left:447px;top:172px"><p class="item-name">Lantern Brewhouse<span class="item-price">$5.25</span></p><p class="item-desc">some of our restaurant menus, prices and special offers may vary.</p></div>

    <aside class="special-panel">
      <p class="special-title">BREAKFAST FOR 2 X1</p>
      <p class="special-item">CAFFE AND PASTRY</p>
      <p class="special-note">some of our restaurant menus, prices and special offers may vary.</p>
      <div class="special-or"><span>OR</span></div>
      <p class="special-item" style="margin-top:8px">COFFEE AN MUFFIN</p>
      <p class="special-note">some of our restaurant menus, prices and special offers may vary.</p>
      <p class="special-served">Both served with fresh milk and all the sweetness we can possibly have</p>
      <div class="seal" role="img" aria-label="Plain round seal"></div>
    </aside>

    <aside class="brand-panel">
      <p class="brand-name">LANTERN<br>BREWHOUSE</p>
      <div class="promo-ring">SPECIAL<br>2X1<br>ASK US</div>
    </aside>
  </section>

  <div class="rule-h" style="left:0;top:293px;width:927px"></div>

  <section class="band band--lunch" aria-label="Lunch">
    <h2 class="section-title" style="left:14px;top:0;height:478px">Lunch</h2>
    <div class="rule-v" style="left:73px;top:0;height:478px"></div>
    <div class="rule-v" style="left:112px;top:0;height:478px;width:1px"></div>
    <h3 class="sub-title" style="left:84px;top:8px;height:136px">Starters</h3>
    <div class="rule-thin" style="left:73px;top:144px;width:745px"></div>
    <h3 class="sub-title" style="left:84px;top:144px;height:197px">Mains</h3>
    <div class="rule-thin" style="left:73px;top:341px;width:854px"></div>
    <h3 class="sub-title" style="left:84px;top:341px;height:137px">Sides</h3>
  </section>

  <div class="item" style="left:126px;top:313px"><p class="item-name">Lantern Brewhouse<span class="item-price">$5.25</span></p><p class="item-desc">some of our restaurant menus, prices and special.</p></div>
  <div class="item" style="left:285px;top:313px"><p class="item-name">Lantern Brewhouse<span class="item-price">$5.25</span></p><p class="item-desc">some of our restaurant menus, prices and special offers may vary.</p></div>
  <div class="item" style="left:445px;top:313px"><p class="item-name">Lantern Brewhouse<span class="item-price">$5.25</span></p><p class="item-desc">some of our restaurant menus, prices and special offers may vary.</p></div>
  <div class="item" style="left:609px;top:313px"><p class="item-name">Lantern Brewhouse<span class="item-price">$5.25</span></p><p class="item-desc">some of our restaurant menus, prices and special offers may vary.</p></div>

  <div class="item" style="left:126px;top:365px"><p class="item-name">Lantern Brewhouse<span class="item-price">$5.25</span></p><p class="item-desc">some of our restaurant menus, prices and special.</p></div>
  <div class="item" style="left:285px;top:378px"><p class="item-name">Lantern Brewhouse<span class="item-price">$5.25</span></p><p class="item-desc">some of our restaurant menus, prices.</p></div>
  <div class="item" style="left:445px;top:378px"><p class="item-name">Lantern Brewhouse<span class="item-price">$5.25</span></p><p class="item-desc">some of our restaurant menus, prices an.</p></div>
  <div class="item" style="left:609px;top:378px"><p class="item-name">Lantern Brewhouse<span class="item-price">$5.25</span></p><p class="item-desc">some of our restaurant menus, prices an.</p></div>

  <p class="fresh-tag">OUR INGREDIENTS<br>ARE FRESH<br>AND PRODUCED<br>LOCALLY</p>

  <div class="item item--wide" style="left:126px;top:462px"><p class="item-name">Lantern Brewhouse<span class="item-price">$5.25</span></p><p class="item-desc">some of our restaurant menus, prices and special offers may vary. our restaurant menus, prices and special.</p></div>
  <div class="item item--wide" style="left:445px;top:462px"><p class="item-name">Lantern Brewhouse<span class="item-price">$5.25</span></p><p class="item-desc">some of our restaurant menus, prices and special offers may vary. our restaurant menus, prices and special.</p></div>
  <div class="item" style="left:776px;top:462px;width:148px"><p class="item-name">Lantern Brewhouse<span class="item-price">$5.25</span></p><p class="item-desc">some of our restaurant menus, prices and special offers may vary.</p></div>

  <div class="item item--wide" style="left:126px;top:515px"><p class="item-name">Lantern Brewhouse<span class="item-price">$5.25</span></p><p class="item-desc">some of our restaurant menus, prices and special offers may vary. our restaurant menus, prices and special.</p></div>
  <div class="item item--wide" style="left:445px;top:515px"><p class="item-name">Lantern Brewhouse<span class="item-price">$5.25</span></p><p class="item-desc">some of our restaurant menus, prices and special offers may vary. our restaurant menus, prices and special.</p></div>

  <div class="item item--wide" style="left:126px;top:570px"><p class="item-name">Lantern Brewhouse<span class="item-price">$5.25</span></p><p class="item-desc">some of our restaurant menus, prices and special offers may vary. our restaurant menus, prices and special.</p></div>
  <div class="item item--wide" style="left:445px;top:570px"><p class="item-name">Lantern Brewhouse<span class="item-price">$5.25</span></p><p class="item-desc">some of our restaurant menus, prices and special offers may vary. our restaurant menus, prices and special.</p></div>

  <div class="tip-box">TIP<br>ASK ABOUT<br>TODAY'S<br>SPECIALS.<br>ALWAYS<br>RESPONSIBLY<br>SOURCED</div>

  <div class="item" style="left:126px;top:655px"><p class="item-name">Lantern Brewhouse<span class="item-price">$5.25</span></p><p class="item-desc">some of our restaurant</p></div>
  <div class="item" style="left:285px;top:655px"><p class="item-name">Lantern Brewhouse<span class="item-price">$5.25</span></p><p class="item-desc">some of our restaurant menus.</p></div>
  <div class="item" style="left:445px;top:655px"><p class="item-name">Lantern Brewhouse<span class="item-price">$5.25</span></p><p class="item-desc">some of our restaurant menus,</p></div>
  <div class="item" style="left:609px;top:655px"><p class="item-name">Lantern Brewhouse<span class="item-price">$5.25</span></p><p class="item-desc">some of our restaurant menus,</p></div>

  <div class="item" style="left:126px;top:696px"><p class="item-name">Lantern Brewhouse<span class="item-price">$5.25</span></p><p class="item-desc">menus, prices and special</p></div>
  <div class="item" style="left:285px;top:706px"><p class="item-name">Lantern Brewhouse<span class="item-price">$5.25</span></p><p class="item-desc">some of our restaurant menus, prices.</p></div>
  <div class="item" style="left:445px;top:706px"><p class="item-name">Lantern Brewhouse<span class="item-price">$5.25</span></p><p class="item-desc">some of our restaurant menus, prices an.</p></div>
  <div class="item" style="left:609px;top:706px"><p class="item-name">Lantern Brewhouse<span class="item-price">$5.25</span></p><p class="item-desc">some of our restaurant menus, prices an.</p></div>

  <div class="rule-h" style="left:0;top:771px;width:927px"></div>

  <section class="band band--drinks" aria-label="Coffee and beverages">
    <h2 class="section-title" style="left:14px;top:0;height:427px;font-size:44px">Coffee/Berverages</h2>
    <div class="rule-v" style="left:73px;top:0;height:427px"></div>
    <div class="rule-v" style="left:112px;top:0;height:427px;width:1px"></div>
    <h3 class="sub-title" style="left:84px;top:0;height:212px">Coffee</h3>
    <div class="rule-thin" style="left:73px;top:212px;width:381px"></div>
    <h3 class="sub-title" style="left:84px;top:212px;height:215px">Berverages</h3>
    <div class="rule-v" style="left:454px;top:0;height:427px;width:1px"></div>
    <div class="rule-v" style="left:810px;top:0;height:427px;width:1px"></div>
  </section>

  <p class="drink" style="left:126px;top:788px">Lantern Brewhouse<span class="item-price">$5.25</span></p>
  <p class="drink" style="left:126px;top:820px">Lantern Brewhouse<span class="item-price">$5.25</span></p>
  <p class="drink" style="left:126px;top:852px">Lantern Brewhouse<span class="item-price">$5.25</span></p>
  <p class="drink" style="left:126px;top:884px">Lantern Brewhouse<span class="item-price">$5.25</span></p>
  <p class="drink" style="left:126px;top:916px">Lantern Brewhouse<span class="item-price">$5.25</span></p>
  <p class="drink" style="left:126px;top:948px">Lantern Brewhouse<span class="item-price">$5.25</span></p>
  <p class="drink" style="left:285px;top:788px">Lantern Brewhouse<span class="item-price">$5.25</span></p>
  <p class="drink" style="left:285px;top:820px">Lantern Brewhouse<span class="item-price">$5.25</span></p>
  <p class="drink" style="left:285px;top:852px">Lantern Brewhouse<span class="item-price">$5.25</span></p>
  <p class="drink" style="left:285px;top:884px">Lantern Brewhouse<span class="item-price">$5.25</span></p>
  <p class="drink" style="left:285px;top:916px">Lantern Brewhouse<span class="item-price">$5.25</span></p>
  <p class="drink-note" style="left:285px;top:940px">with almond milk and cinemon</p>

  <p class="drink" style="left:126px;top:1008px">Lantern Brewhouse<span class="item-price">$5.25</span></p>
  <p class="drink" style="left:126px;top:1040px">Lantern Brewhouse<span class="item-price">$5.25</span></p>
  <p class="drink" style="left:126px;top:1072px">Lantern Brewhouse<span class="item-price">$5.25</span></p>
  <p class="drink" style="left:126px;top:1104px">Lantern Brewhouse<span class="item-price">$5.25</span></p>
  <p class="drink" style="left:126px;top:1136px">Lantern Brewhouse<span class="item-price">$5.25</span></p>
  <p class="drink" style="left:285px;top:1008px">Lantern Brewhouse<span class="item-price">$5.25</span></p>
  <p class="drink" style="left:285px;top:1040px">Lantern Brewhouse<span class="item-price">$5.25</span></p>
  <p class="drink" style="left:285px;top:1072px">Lantern Brewhouse<span class="item-price">$5.25</span></p>
  <p class="drink" style="left:285px;top:1104px">Lantern Brewhouse<span class="item-price">$5.25</span></p>
  <p class="drink" style="left:285px;top:1136px">Lantern Brewhouse<span class="item-price">$5.25</span></p>

  <h2 class="desserts-title">Desserts</h2>

  <div class="item" style="left:474px;top:856px"><p class="item-name">Lantern Brewhouse<span class="item-price">$5.25</span></p><p class="item-desc">some of our restaurant menus, prices and special offers may vary.</p></div>
  <div class="item" style="left:474px;top:916px"><p class="item-name">Lantern Brewhouse<span class="item-price">$5.25</span></p><p class="item-desc">some of our restaurant menus, prices and special offers may vary depending sourced ingredients.</p></div>
  <div class="item" style="left:474px;top:990px"><p class="item-name">Lantern Brewhouse<span class="item-price">$5.25</span></p><p class="item-desc">some of our restaurant menus, prices and special offers may vary depending on locally sourced goodies.</p></div>
  <div class="item" style="left:474px;top:1065px"><p class="item-name">Lantern Brewhouse<span class="item-price">$5.25</span></p><p class="item-desc">some of our restaurant menus, prices and special offers may vary depending on locally sourced goodies.</p></div>

  <div class="item" style="left:647px;top:856px"><p class="item-name">Lantern Brewhouse<span class="item-price">$5.25</span></p><p class="item-desc">some of our restaurant menus, prices and special offers may vary.</p></div>
  <div class="item" style="left:647px;top:916px"><p class="item-name">Lantern Brewhouse<span class="item-price">$5.25</span></p><p class="item-desc">some of our restaurant menus, prices and special offers may vary.</p></div>
  <div class="item" style="left:647px;top:976px"><p class="item-name">Lantern Brewhouse<span class="item-price">$5.25</span></p><p class="item-desc">some of our restaurant menus, prices and special offers may vary.</p></div>

  <div class="dessert-seal" role="img" aria-label="Plain round seal"></div>

  <div class="veggie-flourish" role="img" aria-label="Decorative swirl flourish"></div>
  <p class="veggie-title">Veggie<br>Or<br>Vegan?</p>
  <div class="veggie-flourish veggie-flourish--low" role="img" aria-label="Decorative swirl flourish"></div>
  <p class="veggie-note">ASK ABOUT<br>SPECIAL<br>CUSTOMIZED<br>VEGGY<br>MENUS</p>

</main>
</body>
</html>
```